Square Business Cards for Our Restaurant / Event Venue

We need square business cards designed for the management team of our event venue and restaurant. On one side of the card should be the the Harbor Lantern 7 logo and URL www.harborlantern7.example. On the other side should be the Ember Logo and URL www.emberhall7.example. All employee details should be on the side with Ember logo. There will be a total of 5 cards to be created with the design.

Clara Bennquist
clara@harborlantern7.example

main 555.418.3072
direct 555.730.2946

4831 West Orchard Lane SE
Washington, DC 90417

Industry/Entity Type

Business

```html
<!DOCTYPE html>
<html lang="en">
<head>
<meta charset="utf-8">
<title>Ember / Harbor Lantern 7 — Square Business Cards</title>
<link href="https://fonts.googleapis.com/css2?family=Arimo:wght@400;700&display=swap" rel="stylesheet">
<style>
  :root {
    --backdrop: #dcdcdc;
    --card-white: #ffffff;
    --brand-red: #b41c1e;
    --brand-red-deep: #a5191b;
    --ink: #111111;
    --text-grey: #333333;
  }
  * { margin: 0; padding: 0; box-sizing: border-box; }
  html, body {
    width: 1200px;
    height: 900px;
    overflow: hidden;
    background: var(--backdrop);
    font-family: "Arimo", Arial, sans-serif;
  }
  .sheet { position: relative; width: 1200px; height: 900px; }

  .card {
    position: absolute;
    top: 259px;
    width: 393px;
    height: 393px;
    overflow: hidden;
  }

  /* Front: Ember side with contact details */
  .card--front { left: 197px; background: var(--card-white); }
  .front-edge { position: absolute; inset: 0; width: 393px; height: 393px; }
  .ember-mark {
    position: absolute;
    left: 26px;
    top: 36px;
    font-size: 62px;
    font-weight: 700;
    color: var(--ink);
    line-height: 1;
  }
  .ember-url {
    position: absolute;
    left: 32px;
    top: 135px;
    font-size: 15px;
    color: var(--brand-red);
  }
  .person-name {
    position: absolute;
    left: 24px;
    top: 185px;
    font-size: 24px;
    font-weight: 400;
    color: var(--brand-red);
  }
  .address {
    position: absolute;
    left: 24px;
    top: 244px;
    font-size: 16.5px;
    line-height: 23px;
    color: var(--text-grey);
    font-style: normal;
  }
  .contact-list {
    position: absolute;
    left: 22px;
    top: 302px;
    list-style: none;
    font-size: 16.5px;
    line-height: 23px;
    color: var(--text-grey);
  }
  .contact-label { color: var(--brand-red); font-weight: 700; }

  /* Back: Harbor Lantern 7 side */
  .card--back { left: 614px; }
  .back-field {
    position: absolute;
    inset: 0;
    background: radial-gradient(circle at 50% 45%, var(--brand-red) 0%, var(--brand-red-deep) 100%);
  }
  .lantern-badge {
    position: absolute;
    left: 109px;
    top: 109px;
    width: 174px;
    height: 174px;
    border-radius: 50%;
    background: var(--card-white);
    display: flex;
    align-items: center;
    justify-content: center;
  }
  .lantern-name {
    font-size: 19px;
    font-weight: 400;
    color: var(--brand-red);
    white-space: nowrap;
  }
  .lantern-url {
    position: absolute;
    left: 0;
    right: 0;
    top: 316px;
    text-align: center;
    font-size: 20px;
    color: var(--card-white);
  }
</style>
</head>
<body>
<main class="sheet">

  <section class="card card--front" aria-label="Ember card front">
    <svg class="front-edge" viewBox="0 0 393 393" aria-hidden="true">
      <path d="M393 30 C372 150 346 280 338 393 L393 393 Z" fill="var(--brand-red)"/>
    </svg>
    <div class="ember-mark">Ember</div>
    <div class="ember-url">www.emberhall7.example</div>
    <h1 class="person-name">Clara Bennquist</h1>
    <address class="address">4831 West Orchard Lane SE<br>Washington, DC 90417</address>
    <ul class="contact-list">
      <li><span class="contact-label">P:</span> 555.418.3072</li>
      <li><span class="contact-label">P:</span> 555.730.2946( DIRECT)</li>
      <li><span class="contact-label">E:</span> clara@harborlantern7.example</li>
    </ul>
  </section>

  <section class="card card--back" aria-label="Harbor Lantern 7 card back">
    <div class="back-field" role="img" aria-label="Red background with a faint scattered starburst pattern"></div>
    <div class="lantern-badge"><span class="lantern-name">Harbor Lantern 7</span></div>
    <div class="lantern-url">www.harborlantern7.example</div>
  </section>

</main>
</body>
</html>
```